Simple design for eCommerce retailer of Custom Cut Mirror Frames

We need a fresh design for our eCommerce store. Currently, we need a design for each page on the existing site.

Here is the site as it stands right now: glassvela.com

Here is a competitor site that we like. The owner really likes the block look for the home page: framorly.com

Here is a video we would like to feature: https://videohost.example/v/Kp7rTq2LmXa

Here is the color palate, emphasis on the green and purple: https://palettes.example/quiet-bay-theme-48271953/?showPublished=true

Here is an example of a landing page we are currently using: https://glassvela.com/lander-10-off-install/

Font for the site should be the google font Lato

Home page should include the following sections/blocks:

How it works
Shop now
Testimonials
Featured Products
Before and After Gallery
Updates

My team has been slow getting back to me with feedback. I'm pushing them to speed their process up.

Target Market(s)

Women, Ages 35-65+

Number of Pages Required

5+ page

Font styles to use
Sans Serif

Requirements
Must have
• -Before and after gallery
• -Star ratings
• -eCommerce look and feel
• -Info about being able to order free samples
• -Language from the checkmarks on the landing page
• -sleek product page
• -home page should be have a very modern design feel
Should not have
• Product Prices...the user has to use the calculator to determine the price of their purchase.
• Sliders

```html
<!DOCTYPE html>
<html lang="en">
<head>
<meta charset="utf-8">
<title>GlassVela – Custom Mirror Frame Kits</title>
<link rel="stylesheet" href="https://fonts.googleapis.com/css2?family=Lato:wght@300;400;700&display=swap">
<style>
:root{
  --teal:#5f9c98;
  --teal-light:#8fbfbb;
  --teal-dark:#5a918e;
  --footer:#6aa39f;
  --purple:#a26ea6;
  --purple-block:#a677a9;
  --grey-bg:#eeeeee;
  --ink:#333333;
  --muted:#777777;
  --gold:#f2b705;
  --white:#ffffff;
}
*{box-sizing:border-box;margin:0;padding:0}
html,body{width:1200px;height:2913px;overflow:hidden}
body{font-family:'Lato',sans-serif;color:var(--ink);background:var(--white);position:relative}
.abs{position:absolute}

/* nav */
.site-nav{left:0;top:0;width:1200px;height:45px;background:var(--teal);color:var(--white);font-size:13px;display:flex;align-items:center}
.site-nav .links{display:flex;gap:40px;margin-left:113px}
.site-nav .account{margin-left:auto;margin-right:110px;display:flex;gap:26px;font-size:12px}

/* hero */
.hero{left:0;top:45px;width:1200px;height:456px}
.hero-photo{top:0;height:456px;width:600px}
.hero-photo.before{left:0;background:linear-gradient(180deg,#c9a589 0%,#b48a6c 40%,#6f5644 75%,#3b2e26 100%)}
.hero-photo.after{left:600px;background:linear-gradient(180deg,#d0aa8c 0%,#b9906f 40%,#755a46 75%,#3b2e26 100%)}
.hero-shade{top:0;height:456px;background:rgba(40,40,40,.5)}
.tag{top:205px;padding:6px 14px;font-size:13px;color:var(--white)}
.tag.before{left:358px;background:var(--purple)}
.tag.after{left:777px;background:var(--teal-light)}
.sample-card{left:463px;top:93px;width:276px;height:322px;background:rgba(255,255,255,.95);text-align:center;padding-top:74px}
.brand{display:flex;align-items:center;justify-content:center;gap:8px;font-size:26px;font-weight:700;color:var(--teal)}
.brand .dot{width:14px;height:14px;background:var(--purple)}
.sample-card h2{font-size:18px;font-weight:700;margin-top:38px}
.sample-card p{font-size:14px;margin-top:4px}
.sample-card .guarantee{font-size:12px;margin-top:22px;letter-spacing:.3px}
.btn-outline{display:inline-block;border:1.5px solid var(--purple);color:var(--purple);font-size:13px;padding:8px 18px;margin-top:30px;font-weight:700}
.stars{color:var(--gold);letter-spacing:3px;font-size:13px}

/* intro */
.eyebrow{left:0;width:1200px;top:542px;text-align:center;font-size:19px;font-weight:400}
.section-title{left:0;width:1200px;top:566px;text-align:center;font-size:33px;font-weight:300;color:var(--purple);letter-spacing:1px}
.video{left:113px;top:647px;width:470px;height:270px;background:linear-gradient(135deg,#c9cdd6,#8a8f9e 55%,#3e4152)}
.video .play{left:206px;top:112px;width:54px;height:38px;background:#222;border-radius:8px}
.video .bar{left:0;bottom:0;width:470px;height:22px;background:rgba(0,0,0,.75);color:#ddd;font-size:10px;padding:5px 10px}
.intro-copy{left:611px;top:640px;width:466px;font-size:13.3px;line-height:23.6px;color:var(--muted)}

.checklist{top:985px;list-style:none;font-size:13.5px;color:#555}
.checklist li{display:flex;align-items:center;gap:8px;height:44px}
.checklist.one{left:113px}
.checklist.two{left:402px}
.tick{width:12px;height:12px}

.promise{left:695px;top:990px;width:393px;height:245px;background:linear-gradient(135deg,#3a3a3a,#1f1f1f);text-align:center;color:var(--white)}
.ribbon{left:0;top:36px;width:393px}
.ribbon .band{margin:0 auto;width:340px;background:#57b3a7;font-size:16px;padding:7px 0;letter-spacing:.5px}
.promise p{position:absolute;top:96px;left:0;width:393px;font-size:15px;font-weight:700;line-height:25px}
.btn-light{position:absolute;left:112px;top:162px;width:170px;border:1.5px solid #ccc;font-size:14px;padding:10px 0;font-weight:700}

/* blocks */
.blocks{left:0;top:1295px;width:1200px;height:1055px;background:var(--grey-bg)}
.block{color:var(--white);text-align:center}
.block h3{font-weight:300;font-size:24px;letter-spacing:1px;margin-top:32px}
.how{left:113px;top:1355px;width:474px;height:376px;background:var(--teal-light)}
.featured{left:614px;top:1355px;width:474px;height:376px;background:var(--purple-block)}
.reviews{left:113px;top:1757px;width:474px;height:538px;background:linear-gradient(180deg,#3f3f3f,#2a2a2a)}
.gallery{left:614px;top:1757px;width:474px;height:538px;background:var(--teal-dark)}

.product-photo{left:82px;top:84px;width:310px;height:206px;background:linear-gradient(135deg,#6b6259,#b8b3ad 30%,#d7dbe0 60%,#c6cbd1)}
.product-name{left:82px;top:250px;width:310px;font-size:13px;color:#333}
.product-name .stars{display:block;margin-top:2px}
.arrow{top:160px;font-size:34px;font-weight:300}
.btn-white{position:absolute;left:122px;top:310px;width:230px;border:1.5px solid rgba(255,255,255,.85);font-size:14px;padding:9px 0}

.reviews blockquote{position:absolute;left:56px;top:160px;width:385px;text-align:left;font-size:15px;line-height:26px}
.reviews .who{position:absolute;left:0;top:266px;width:474px;font-size:12px;color:#ddd}
.reviews .stars{position:absolute;left:0;top:288px;width:474px}
.pager{top:352px;width:32px;height:32px;border-radius:50%;background:#222;color:#aaa;font-size:14px;line-height:32px}

.gallery h3{line-height:31px;margin-top:0;padding-top:34px}
.thumb{width:200px;height:143px}
.btn-white.wide{top:455px;left:130px;width:214px;font-size:13px}

/* footer */
.site-footer{left:0;top:2350px;width:1200px;height:563px;background:var(--footer);color:var(--white)}
.site-footer .brand{color:var(--white);position:absolute;top:82px;left:0;width:1200px}
.contact{top:162px;font-size:14px;text-align:center}
.contact .icon{height:36px;display:flex;align-items:center;justify-content:center;margin-bottom:16px}
.foot-row{left:113px;width:980px;display:flex;font-size:12px;align-items:center}
.foot-row .label{width:294px;font-weight:700;font-size:15px}
.foot-row .items{display:flex;gap:32px}
.badge{top:2758px;width:66px;height:66px;background:#fff}
.copyright{top:2868px;left:0;width:1200px;text-align:center;font-size:11px;color:var(--white)}
</style>
</head>
<body>

<nav class="site-nav abs">
  <div class="links"><span>Home</span><span>Shop Mirror Frames</span><span>Custom Framed Mirrors</span><span>How It Works</span><span>Before &amp; After Gallery</span></div>
  <div class="account"><span>My account</span><span>Cart(0)</span></div>
</nav>

<header class="hero abs">
  <div class="hero-photo before abs" role="img" aria-label="Bathroom vanity mirror without a frame"></div>
  <div class="hero-photo after abs" role="img" aria-label="Same bathroom mirror with a custom frame added"></div>
  <div class="hero-shade abs" style="left:463px;width:276px;background:rgba(30,30,30,.55)"></div>
  <span class="tag before abs">Before</span>
  <span class="tag after abs">After</span>
</header>

<section class="sample-card abs">
  <div class="brand"><span class="dot"></span>GlassVela</div>
  <h2>Get up to 7 Samples FREE!</h2>
  <p>Use code: freesample at checkout.</p>
  <p class="guarantee">100% SATISFACTION GUARANTEE!</p>
  <span class="btn-outline">GET A FREE SAMPLE CODE</span>
  <div class="stars" style="margin-top:-4px">★★★★★</div>
</section>

<p class="eyebrow abs">Quick, Easy, and Affordable</p>
<h1 class="section-title abs">CUSTOM MIRROR FRAME KITS</h1>

<div class="video abs" role="img" aria-label="Video of a woman fitting a frame onto a bathroom mirror">
  <div class="play abs"><svg width="54" height="38"><polygon points="22,12 22,26 33,19" fill="#fff"/></svg></div>
  <div class="bar abs">0:00 / 3:24</div>
</div>

<p class="intro-copy abs">With residential construction costs rising, contractors and homeowners often choose to install sheet glass mirrors in bathrooms and living spaces. While this is functional and economical, these mirrors often lack a unique style and décor enhancement of a hanging custom mirror frame. Instead, get Custom Framed Mirrors built to your specifications. Simply choose your style and enter your size. We have many mirror frame kits to fit your needs. Whether you are looking for one mirror frame or several mirror frames, we can make your mirrors look custom and revitalized. So whether you are looking to refresh your bathroom mirror or any mirror in your house – Our custom mirror frame kit is easy to install too. So be like Snow White and say “mirror mirror” and you too can breathe new life into your bathroom mirror.</p>

<ul class="checklist one abs">
  <li><svg class="tick"><path d="M1 1h10L6 6z" fill="#a26ea6"/><path d="M1 1v10" stroke="#a26ea6" stroke-width="2"/></svg>DIY mirror framing kit</li>
  <li><svg class="tick"><path d="M1 1h10L6 6z" fill="#a26ea6"/><path d="M1 1v10" stroke="#a26ea6" stroke-width="2"/></svg>Install with mirror still on wall</li>
  <li><svg class="tick"><path d="M1 1h10L6 6z" fill="#a26ea6"/><path d="M1 1v10" stroke="#a26ea6" stroke-width="2"/></svg>Style selections to match any home decor</li>
  <li><svg class="tick"><path d="M1 1h10L6 6z" fill="#a26ea6"/><path d="M1 1v10" stroke="#a26ea6" stroke-width="2"/></svg>Beveled Mirrors? No problem!</li>
  <li><svg class="tick"><path d="M1 1h10L6 6z" fill="#a26ea6"/><path d="M1 1v10" stroke="#a26ea6" stroke-width="2"/></svg>Guaranteed to fit any mirror, any size</li>
</ul>
<ul class="checklist two abs">
  <li><svg class="tick"><path d="M1 1h10L6 6z" fill="#a26ea6"/><path d="M1 1v10" stroke="#a26ea6" stroke-width="2"/></svg>Extends beyond mirror to hide ugly edges</li>
  <li><svg class="tick"><path d="M1 1h10L6 6z" fill="#a26ea6"/><path d="M1 1v10" stroke="#a26ea6" stroke-width="2"/></svg>DIY Install within minutes</li>
  <li><svg class="tick"><path d="M1 1h10L6 6z" fill="#a26ea6"/><path d="M1 1v10" stroke="#a26ea6" stroke-width="2"/></svg>100% Satisfaction Guarantee</li>
  <li><svg class="tick"><path d="M1 1h10L6 6z" fill="#a26ea6"/><path d="M1 1v10" stroke="#a26ea6" stroke-width="2"/></svg>Outstanding customer support</li>
</ul>

<aside class="promise abs">
  <div class="ribbon abs"><div class="band">100% SATISFACTION GUARANTEE!</div></div>
  <p>Unsure? – Don't Worry, We Will Walk You<br>Through Every Step Of The Process.</p>
  <span class="btn-light">Shop Now Free Sample</span>
</aside>

<div class="blocks abs"></div>

<section class="block how abs">
  <h3>HOW IT WORKS</h3>
  <svg class="abs" style="left:0;top:0" width="474" height="376">
    <line x1="237" y1="90" x2="237" y2="345" stroke="#fff" stroke-width="2"/>
    <g font-family="Lato,sans-serif" font-size="11" font-weight="700" fill="#fff" text-anchor="middle">
      <circle cx="237" cy="130" r="23" fill="#c592c2"/><text x="237" y="127">Step</text><text x="237" y="140">1</text>
      <circle cx="237" cy="197" r="23" fill="#c592c2"/><text x="237" y="194">Step</text><text x="237" y="207">2</text>
      <circle cx="237" cy="265" r="23" fill="#c592c2"/><text x="237" y="262">Step</text><text x="237" y="275">3</text>
    </g>
    <line x1="260" y1="197" x2="272" y2="197" stroke="#fff" stroke-width="2"/><circle cx="275" cy="197" r="4" fill="#fff"/>
    <line x1="214" y1="130" x2="202" y2="130" stroke="#fff" stroke-width="2"/><circle cx="199" cy="130" r="4" fill="#fff"/>
    <line x1="214" y1="265" x2="202" y2="265" stroke="#fff" stroke-width="2"/><circle cx="199" cy="265" r="4" fill="#fff"/>
    <rect x="108" y="108" width="70" height="44" fill="#d8b43a" opacity=".8" role="img" aria-label="Tape measure"/>
    <polygon points="330,164 350,146 370,164 362,164 350,153 338,164" fill="#333"/>
    <polygon points="330,184 350,166 370,184 362,184 350,173 338,184" fill="#333"/>
    <rect x="112" y="240" width="58" height="44" fill="#d6d9de" role="img" aria-label="Person installing a frame"/>
    <g font-family="Lato,sans-serif" font-size="13" font-weight="700" fill="#222">
      <text x="78" y="178">Measure Your Mirror</text>
      <text x="305" y="222">Choose A Frame</text>
      <text x="64" y="310">Easy No Tools Installation</text>
    </g>
  </svg>
</section>

<section class="block featured abs">
  <h3>FEATURED PRODUCT</h3>
  <div class="product-photo abs" role="img" aria-label="Corner of a mirror with a contemporary silver frame"></div>
  <div class="product-name abs">CONTEMPORARY SILVER<span class="stars">★★★★★</span></div>
  <span class="arrow abs" style="left:52px">‹</span>
  <span class="arrow abs" style="right:52px">›</span>
  <span class="btn-white">Shop all Frames</span>
</section>

<section class="block reviews abs" role="group" aria-label="Customer testimonials">
  <h3>WHAT OUR CUSTOMERS ARE SAYING</h3>
  <blockquote>Great product and great service! Adding frames to our mirrors made all the difference in how the master bath looks. You can't beat GlassVela for the money!</blockquote>
  <div class="who">Dana R., Brookhaven, Ca</div>
  <div class="stars">★★★★★</div>
  <span class="pager abs" style="left:196px">‹</span>
  <span class="pager abs" style="left:244px">›</span>
</section>

<section class="block gallery abs">
  <h3>CUSTOMER BEFORE/AFTER<br>MIRROR FRAME KIT PHOTOS</h3>
  <div class="thumb abs" style="left:36px;top:125px;background:linear-gradient(180deg,#efe6da,#8a6c55)" role="img" aria-label="Vanity mirror before framing"></div>
  <div class="thumb abs" style="left:239px;top:125px;background:linear-gradient(180deg,#ece4d8,#4a3a30)" role="img" aria-label="Vanity mirror after dark frame added"></div>
  <div class="thumb abs" style="left:36px;top:271px;background:linear-gradient(180deg,#e7c9a6,#a77c58)" role="img" aria-label="Bathroom mirror before framing"></div>
  <div class="thumb abs" style="left:239px;top:271px;background:linear-gradient(180deg,#e6c6a2,#8d6846)" role="img" aria-label="Bathroom mirror after wood frame added"></div>
  <span class="btn-white wide">BEFORE &amp; AFTER GALLERY</span>
</section>

<footer class="site-footer abs">
  <div class="brand"><span class="dot" style="background:#fff"></span>GlassVela</div>

  <div class="contact abs" style="left:88px;width:360px">
    <div class="icon"><svg width="26" height="34"><path d="M13 32C5 20 2 15 2 11a11 11 0 0 1 22 0c0 4-3 9-11 21z" fill="none" stroke="#fff" stroke-width="2"/><circle cx="13" cy="11" r="4" fill="none" stroke="#fff" stroke-width="2"/></svg></div>
    812 Harbor Mill Road, Suite 4, Alderport, CA 90417
  </div>
  <div class="contact abs" style="left:525px;width:200px">
    <div class="icon"><svg width="30" height="30"><path d="M6 3l6 6-3 4c2 4 5 7 9 9l4-3 6 6-4 4C13 28 2 17 2 7z" fill="none" stroke="#fff" stroke-width="2"/></svg></div>
    (555) 014-2290
  </div>
  <div class="contact abs" style="left:831px;width:240px">
    <div class="icon"><svg width="32" height="24"><rect x="1" y="1" width="30" height="22" fill="none" stroke="#fff" stroke-width="2"/><path d="M1 1l15 12L31 1" fill="none" stroke="#fff" stroke-width="2"/></svg></div>
    support@glassvela.com
  </div>

  <div class="foot-row abs" style="top:270px"><span class="label">COMPANY INFO</span><span class="items"><span>GlassVela.com</span><span>About Us</span><span>Privacy Policy</span><span>Terms &amp; Condition</span><span>Security on Our Site</span></span></div>
  <div class="foot-row abs" style="top:307px"><span class="label">POLICIES &amp; PRODUCT INFO</span><span class="items"><span>Our Gurantee</span><span>Shipping</span><span>Product Care</span><span>Return Policy</span></span></div>
  <div class="foot-row abs" style="top:345px"><span class="label">SERVICES &amp; SUPPORT</span><span class="items"><span>FAQ</span><span>Customer Support</span><span>Contact Us</span></span></div>
</footer>

<div class="badge abs" style="left:524px" aria-hidden="true"></div>
<div class="badge abs" style="left:607px" aria-hidden="true"></div>
<p class="copyright abs">© Copyright 2019 &nbsp;|&nbsp; GlassVela.com &nbsp;|&nbsp; All Rights Reserved &nbsp;|&nbsp; Website by Lanternfish Studio</p>

</body>
</html>
```